We need a logo for our business which is a dental clinic (i.e. dentistry).
We would lilke designs using the colour blue, green and black incorporating the words Corvath Dental, possibly a smile or a tooth image can be considered for incorporation in the logo.

Industry/Entity Type

Dental

```html
<!DOCTYPE html>
<html lang="en">
<head>
<meta charset="utf-8">
<title>Corvath Dental – Business Cards</title>
<link rel="stylesheet" href="https://fonts.googleapis.com/css2?family=Open+Sans:wght@400;600&display=swap">
<style>
  :root {
    --backdrop: #2b2b2b;
    --card: #ffffff;
    --ink: #231f20;
    --brand-blue: #29a8e0;
    --brand-green: #1fa37a;
    --band: #141414;
    --band-text: #ffffff;
  }
  * { box-sizing: border-box; margin: 0; padding: 0; }
  html, body {
    width: 1200px; height: 599px; overflow: hidden;
    background: var(--backdrop);
    font-family: "Open Sans", Arial, sans-serif;
  }
  .stage { position: relative; width: 1200px; height: 599px; }
  .card {
    position: absolute;
    width: 560px; height: 320px;
    background: var(--card);
    border-radius: 28px;
    overflow: hidden;
  }
  .card--front { left: 30px; top: 50px; }
  .card--back  { left: 610px; top: 220px; }

  .brand {
    position: absolute;
    display: flex; align-items: center; gap: 14px;
    color: var(--ink);
    font-weight: 600;
    font-size: 44px;
    line-height: 1;
    white-space: nowrap;
  }
  .brand__dot {
    width: 22px; height: 22px; border-radius: 50%;
    background: var(--brand-blue);
    flex: none;
  }
  .card--front .brand { left: 120px; top: 95px; }
  .card--back .brand  { left: 95px; top: 120px; font-size: 50px; }

  .holder {
    position: absolute; left: 0; right: 0; top: 180px;
    text-align: center; padding-left: 120px;
    line-height: 1.3;
  }
  .holder__name { color: var(--brand-blue); font-weight: 600; font-size: 19px; }
  .holder__role { color: var(--ink); font-size: 11px; letter-spacing: .5px; }

  .band { position: absolute; left: 0; bottom: 0; width: 100%; height: 90px; }
  .band svg { display: block; width: 100%; height: 100%; }

  .contact {
    position: absolute; left: 0; right: 0; bottom: 12px;
    color: var(--band-text); font-size: 12px; line-height: 1.6;
    text-align: center; padding-left: 60px;
  }
  .web {
    position: absolute; left: 0; right: 0; bottom: 22px;
    color: var(--band-text); font-size: 13px; text-align: center;
  }
</style>
</head>
<body>
<div class="stage">

  <section class="card card--front">
    <div class="brand"><span class="brand__dot"></span>Corvath Dental</div>
    <div class="holder">
      <p class="holder__name">Name Here</p>
      <p class="holder__role">DIRECTOR | OWNER</p>
    </div>
    <div class="band">
      <svg viewBox="0 0 560 90" preserveAspectRatio="none">
        <path d="M0 52 Q280 4 560 22 L560 90 L0 90 Z" fill="var(--brand-green)"/>
        <path d="M0 58 Q280 10 560 28 L560 90 L0 90 Z" fill="var(--band)"/>
      </svg>
    </div>
    <div class="contact">
      <p>Address Line1, Address Line2, City, Zip code</p>
      <p>Phone: 000 000 0000 | Fax: 000 000 0000 | Mail: info@corvathdental.com</p>
    </div>
  </section>

  <section class="card card--back">
    <div class="brand"><span class="brand__dot"></span>Corvath Dental</div>
    <div class="band">
      <svg viewBox="0 0 560 90" preserveAspectRatio="none">
        <path d="M0 18 Q280 10 560 62 L560 90 L0 90 Z" fill="var(--brand-green)"/>
        <path d="M0 24 Q280 16 560 68 L560 90 L0 90 Z" fill="var(--band)"/>
      </svg>
    </div>
    <p class="web">www.corvathdental.com</p>
  </section>

</div>
</body>
</html>
```